Brindle Advisory Business Card Design

Business card for business consulting company, using attached logo. We do financial and strategic consulting, and want a clean, professional image with a bit of fun. Our logo is a flat whale tail, which symbolizes the Orca whale, a highly collaborative, group based animal that is very successful in navigating the ocean, protecting the herd, and hunting. We like the logo that is blue and gray on white one one side, but would be open to a blue card with white lettering on the other side... or whatever you'd suggest
Updates
Hi all - I have had the logo modified to take the shadowing off the tail. I will post it on the brief... under a file name called updated logo. thank you Added Saturday, April 25, 2015
Target Market(s)
Small to medium sized businesses ($10M to $500M in revenue per year), financial and sales executives, general managers, attorneys and CPAs
Industry/Entity Type
Financial
Contact Information for Business Card
Want company name, contact info - name, title, telephone, email, website, linkedin, twitter and Facebook. No physical address yet.
Requirements
Must have
- contemporary design, bold, strong, confident but with a bit of fun. prominently feature the logo and the whale tail icon
Nice to have
- unique touches that would differentiate us from a regular card... for example, logo and writing all on front on white background, but on back - logo in white on a blue background
- open to idea of different shapes of card than standard... but not sure
Should not have
- ?

```html
<!DOCTYPE html>
<html lang="en">
<head>
<meta charset="utf-8">
<title>Brindle Advisory – Business Card</title>
<link rel="stylesheet" href="https://fonts.googleapis.com/css2?family=Exo+2:wght@400;600;700&display=swap">
<style>
  :root {
    --navy: #0f3468;
    --paper: #ffffff;
    --paper-shade: #f3f4f5;
    --rail: #c9cbcd;
    --ink-grey: #8a8d90;
    --stage: #2b2b2c;
  }
  * { box-sizing: border-box; margin: 0; padding: 0; }
  html, body { width: 1200px; height: 944px; overflow: hidden; }
  body {
    background: var(--stage);
    font-family: "Exo 2", sans-serif;
    display: flex;
    align-items: center;
    justify-content: center;
    gap: 80px;
  }
  .card {
    position: relative;
    width: 370px;
    height: 640px;
    overflow: hidden;
  }
  .card-shape { position: absolute; inset: 0; }

  .brand {
    position: absolute;
    top: 92px;
    left: 0;
    right: 0;
    display: flex;
    flex-direction: column;
    align-items: center;
  }
  .brand-mark {
    display: flex;
    align-items: center;
    gap: 12px;
  }
  .brand-square {
    width: 34px;
    height: 34px;
    background: var(--navy);
    border-radius: 5px;
  }
  .brand-name {
    font-weight: 700;
    font-size: 31px;
    color: var(--navy);
    letter-spacing: -0.5px;
    white-space: nowrap;
  }
  .brand-tagline {
    align-self: flex-end;
    margin-right: 48px;
    margin-top: 2px;
    font-size: 12px;
    color: var(--ink-grey);
    font-style: italic;
  }

  .person {
    position: absolute;
    top: 300px;
    left: 46px;
    color: var(--paper);
  }
  .person-name {
    font-weight: 700;
    font-size: 32px;
    letter-spacing: 1px;
    text-transform: uppercase;
  }
  .person-title {
    font-weight: 400;
    font-size: 19px;
    letter-spacing: 2.5px;
    text-transform: uppercase;
    margin-top: 2px;
  }

  .contacts {
    position: absolute;
    top: 408px;
    left: 46px;
    list-style: none;
    color: var(--paper);
    font-size: 14px;
    letter-spacing: 0.5px;
  }
  .contact {
    display: flex;
    align-items: center;
    gap: 10px;
    height: 29px;
    white-space: nowrap;
  }
  .contact-icon {
    width: 18px;
    height: 18px;
    flex: none;
  }

  .card-back { background: var(--navy); }
  .back-brand {
    position: absolute;
    inset: 0;
    display: flex;
    flex-direction: column;
    align-items: center;
    justify-content: center;
    gap: 18px;
  }
  .back-square {
    width: 64px;
    height: 64px;
    background: var(--paper);
    border-radius: 8px;
  }
  .back-name {
    font-weight: 700;
    font-size: 34px;
    color: var(--paper);
    letter-spacing: -0.5px;
    white-space: nowrap;
  }
</style>
</head>
<body>

  <article class="card card-front" aria-label="Business card front">
    <svg class="card-shape" viewBox="0 0 370 640" aria-hidden="true">
      <rect width="370" height="640" fill="var(--paper)"/>
      <rect width="370" height="225" fill="var(--paper-shade)"/>
      <polygon points="0,250 30,225 340,225 370,250 370,620 0,620" fill="var(--rail)"/>
      <polygon points="22,262 46,240 324,240 348,262 348,600 22,600" fill="var(--navy)"/>
      <rect y="620" width="370" height="20" fill="var(--paper)"/>
    </svg>

    <header class="brand">
      <div class="brand-mark">
        <span class="brand-square"></span>
        <span class="brand-name">Brindle Advisory</span>
      </div>
      <span class="brand-tagline">business consulting</span>
    </header>

    <div class="person">
      <h1 class="person-name">Daniel Reyes</h1>
      <p class="person-title">General Manager</p>
    </div>

    <ul class="contacts">
      <li class="contact">
        <svg class="contact-icon" viewBox="0 0 18 18" aria-hidden="true">
          <circle cx="9" cy="9" r="9" fill="#fff"/>
          <path d="M6 4.5l1.6 2.4-1 1.1c.6 1.3 1.6 2.3 2.9 2.9l1.1-1 2.4 1.6-.8 1.8c-3.6-.4-6.6-3.4-7-7z" fill="var(--navy)"/>
        </svg>
        014 382 5590
      </li>
      <li class="contact">
        <svg class="contact-icon" viewBox="0 0 18 18" aria-hidden="true">
          <circle cx="9" cy="9" r="9" fill="#fff"/>
          <rect x="6" y="3.5" width="6" height="11" rx="1.2" fill="var(--navy)"/>
          <rect x="7" y="5" width="4" height="6.5" fill="#fff"/>
        </svg>
        014 382 5591
      </li>
      <li class="contact">
        <svg class="contact-icon" viewBox="0 0 18 18" aria-hidden="true">
          <circle cx="9" cy="9" r="9" fill="#fff"/>
          <rect x="4" y="5.5" width="10" height="7" fill="var(--navy)"/>
          <path d="M4 5.5l5 4 5-4" fill="none" stroke="#fff" stroke-width="1"/>
        </svg>
        dreyes@brindlemail.com
      </li>
      <li class="contact">
        <svg class="contact-icon" viewBox="0 0 18 18" aria-hidden="true">
          <circle cx="9" cy="9" r="9" fill="#fff"/>
          <circle cx="9" cy="9" r="5" fill="none" stroke="var(--navy)" stroke-width="1.2"/>
          <ellipse cx="9" cy="9" rx="2" ry="5" fill="none" stroke="var(--navy)" stroke-width="1.2"/>
          <line x1="4" y1="9" x2="14" y2="9" stroke="var(--navy)" stroke-width="1.2"/>
        </svg>
        www.brindleadvisory.com
      </li>
      <li class="contact">
        <svg class="contact-icon" viewBox="0 0 18 18" aria-hidden="true">
          <circle cx="9" cy="9" r="9" fill="#fff"/>
          <circle cx="9" cy="9" r="3.5" fill="var(--navy)"/>
        </svg>
        @brindleadvisory
      </li>
    </ul>
  </article>

  <article class="card card-back" aria-label="Business card back">
    <div class="back-brand">
      <span class="back-square"></span>
      <span class="back-name">Brindle Advisory</span>
    </div>
  </article>

</body>
</html>
```